依頼詳細
コーディング等の作業はございません。載せたい項目・文章関係・動線については添付ラフの内容です。
ビジュアルのみの募集になりますが、もっと良くなりそうなご提案があれば変更してください。

下記の点を求めています。
・コンサル会社のサイトのようなイメージに変えたい!(経験豊富な専任コンサルタントがつき、いろいろアドバイスしてくれるので安心!)(忙しいお客さんや予算と実施のみが決まっているだけで具体的な提案を欲しがっているようなお客さんや納期がなく困っているお客さん等いろんなお客さんからの相談窓口)がほしい。
・自分で探したい人は、色んな用途で探しやすいサイトにしたい。(2軸のコンセプトのサイトを目指しています。)
・イメージカラーは、白ベースに赤

ターゲットは、25~45歳位の企業の販促担当者になります。
男女比は、半々程度です。

下記のようなサイトがいいと思っています。
https://torivane.net/
http://www.kumolo.jp/
サイトURL
http://www.sk-shokai.com/
ページ数
1ページ
希望イメージ
• +5 0 +5
• シンプル
複雑
• 単色
カラフル
• 暗い
明るい
• 日常
高級
• 遊び心
厳粛
• 未来的
伝統的
• 女性的
男性的
希望する色
赤系
納品ファイル
• イラストレーター形式 (.ai)
• フォトショップ形式 (.psd)
補足説明
・メリハリのある見やすいページにしたいです・
・頼りになる販促コンサルタントにおまかせできる(販促コンサルタントのブランディングをしっかりしたい)
・相談したくないもしくは相談前に自分で商品を探してみたい

この3点をしっかり表現出来ているサイトへのリニューアルを目指しています。

よろしくお願いいたします。
依頼公開後の追記内容
プロモエリアのコピーですが、

販促×お悩み相談!=集客商会

で、お願いします。
※もっといいご提案があれば変えていただいても大丈夫です。
必須ではありません。
当社の取扱商品や現在Web上で使用している素材が制作に必要な場合、
下記からダウンロードいただけます。

http://qv7.link/TpAx
パスワード:7wqe

今回の応募作品で制作していただく以外の目的には使用しないように
お願いいたします。
ダウンロード期限:2017年11月9日(木)

より大きいサイズの画像が必要な場合、
同じものをご用意できない可能性もありますが、ご相談くださいませ。
上記サンプルファイルのダウンロード期限が過ぎましたので
再びアップロードいたします。

http://rr828rr.info/K4mb
ダウンロード期限:2017年11月20日(月)

応募の期限は残り僅かですがどうぞよろしくお願いいたします。
■ 選んだ理由

お仕事が丁寧で、デザインもスッキリしていて、且つ訴求ポイントのわかりやすさとのバランスがとても気に入りました。

修正依頼に対するレスもとても早く助かりました。
また、機会がございましたらお願いできたら嬉しいです。
この度は、ありがとうございました。

■ 提案者全員のお礼・コメント

この度は弊社の集客商会のデザインコンペに参加いただき、誠にありがとうございました。
前回、集まりが悪いと思ってしまい途中で取り下げてしまったことが間違いだったと再認識しました。
今回も応募作品のレベルが高く選考するのにかなり迷ってしまいました。
選べなかった作品も素晴い作品が多くありました。
今回ご応募いただいた方々に感謝です。

ありがとうございました。
また、募集の機会がございましたら宜しくお願い致します。

```html
<!DOCTYPE html>
<html lang="ja">
<head>
<meta charset="utf-8">
<title>集客商会 | ノベルティ・オリジナルグッズ制作</title>
<link href="https://fonts.googleapis.com/css2?family=Noto+Sans+JP:wght@400;500;700;900&family=Roboto:wght@400;700;900&display=swap" rel="stylesheet">
<style>
:root{
  --red:#d7000f;
  --ink:#333333;
  --muted:#777777;
  --line:#dddddd;
  --pale:#f3f3f3;
  --pale-2:#e9e9e9;
  --white:#ffffff;
  --sns-1:#c13584;
  --sns-2:#3b5998;
  --sns-3:#1da1f2;
  --sns-4:#d92323;
}
*{box-sizing:border-box;margin:0;padding:0}
html,body{width:1200px;height:4352px;overflow:hidden}
body{font-family:"Noto Sans JP",sans-serif;color:var(--ink);background:var(--white);font-size:14px;line-height:1.5}
ul{list-style:none}
.en{font-family:"Roboto",sans-serif}

/* header */
.site-header{height:140px;display:flex;align-items:center;justify-content:space-between;padding:0 40px}
.brand{display:flex;align-items:center;gap:14px}
.brand-mark{width:80px;height:80px;background:var(--red)}
.brand-name{font-size:48px;font-weight:900;color:var(--red);letter-spacing:2px}
.brand-tag{font-size:12px;color:var(--muted);margin-left:10px;align-self:flex-end;padding-bottom:16px}
.contact{text-align:right}
.contact small{display:block;font-size:11px;color:var(--muted)}
.contact .tel{display:flex;align-items:center;gap:8px;justify-content:flex-end;font-size:36px;font-weight:700;color:var(--red);font-family:"Roboto",sans-serif;line-height:1.1}
.contact .hours{font-size:11px;color:var(--muted)}
.global-nav{height:60px;border-top:1px solid var(--line);border-bottom:3px solid var(--red);display:flex;justify-content:center}
.global-nav a{display:flex;align-items:center;padding:0 26px;font-size:14px;color:var(--ink);text-decoration:none;border-left:1px solid var(--line)}
.global-nav a:last-child{border-right:1px solid var(--line)}

/* hero */
.hero{margin-top:20px;height:560px;background:linear-gradient(180deg,#f7f7f7,#e6e6e6);position:relative;overflow:hidden}
.hero-goods{position:absolute;left:50px;top:40px;width:360px;height:480px;background:linear-gradient(135deg,#c9dce8,#f0c9a4 55%,#e8e0b0)}
.hero-person{position:absolute;right:50px;top:30px;width:330px;height:530px;background:linear-gradient(180deg,#e7d6c8,#c9b6a6)}
.hero-copy{position:absolute;left:0;right:0;top:210px;text-align:center;z-index:2}
.hero-copy p{display:inline-block;font-size:20px;font-weight:700;background:rgba(255,255,255,.85);padding:4px 18px}
.hero-copy h1{display:block;width:max-content;margin:18px auto 0;font-size:58px;font-weight:900;color:var(--red);letter-spacing:1px;white-space:nowrap;background:rgba(255,255,255,.85);padding:4px 24px;line-height:1.3}
.hero-badge{position:absolute;right:330px;top:40px;width:130px;height:130px;border-radius:50%;background:var(--red);color:var(--white);display:flex;flex-direction:column;align-items:center;justify-content:center;font-weight:700;font-size:15px;z-index:3}
.hero-badge strong{font-size:24px;font-family:"Roboto",sans-serif}

/* consultants */
.consult{display:grid;grid-template-columns:1fr 1fr 1fr;gap:20px;padding:30px 40px 0;height:220px}
.consult-card{background:var(--pale);display:flex;align-items:center;gap:16px;padding:14px;border:1px solid var(--line)}
.consult-card .photo{width:140px;height:160px;background:linear-gradient(180deg,#d9d3cc,#9aa2ad);flex:none}
.consult-card .label{display:inline-block;background:var(--red);color:var(--white);font-size:12px;padding:2px 8px;margin-bottom:6px}
.consult-card p{font-size:19px;font-weight:700;line-height:1.4}
.consult-card.center{justify-content:center;text-align:center;background:#eef0f2}
.consult-card.center p{font-size:22px}

/* body columns */
.columns{display:flex;gap:26px;padding:30px 40px 0;height:2000px;overflow:hidden}
.sidebar{width:250px;flex:none}
.main{flex:1;min-width:0}
.side-head{background:var(--ink);color:var(--white);font-weight:700;font-size:15px;padding:9px 12px}
.side-head.red{background:var(--red)}
.cat-list li{display:flex;align-items:center;gap:10px;height:34px;border-bottom:1px solid var(--line);font-size:13px;padding-left:6px}
.cat-list .thumb{width:24px;height:24px;background:var(--pale-2);flex:none}
.plain-list li{height:30px;border-bottom:1px dotted var(--line);font-size:13px;padding:5px 8px}
.plain-list li::before{content:"›";color:var(--red);margin-right:6px}
.side-block{margin-top:22px}
.side-toggle{margin-top:10px;border:1px solid var(--line);padding:10px 12px;font-size:14px;font-weight:700;display:flex;justify-content:space-between}
.sns-stack{margin-top:22px;display:grid;gap:8px}
.sns-btn{height:44px;display:flex;align-items:center;gap:10px;padding:0 12px;color:var(--white);font-weight:700;font-size:14px}
.sns-btn i{width:16px;height:16px;background:rgba(255,255,255,.85);display:block;flex:none}

.banners{display:grid;grid-template-columns:1fr 1fr 1fr;gap:12px;height:210px}
.banners div{display:flex;align-items:flex-end;padding:12px;font-weight:700;font-size:16px;color:var(--white)}
.section-head{display:flex;align-items:baseline;gap:12px;border-bottom:2px solid var(--red);padding-bottom:6px;margin-top:40px}
.section-head h2{font-family:"Roboto",sans-serif;font-size:26px;font-weight:900}
.section-head span{font-size:13px;color:var(--muted)}
.achievement{display:flex;gap:16px;margin-top:18px;height:160px;align-items:stretch}
.case-label{width:70px;background:var(--red);color:var(--white);font-family:"Roboto",sans-serif;font-weight:700;display:flex;align-items:center;justify-content:center}
.case-photo{width:240px;background:linear-gradient(135deg,#9fb8cc,#d8e3ea)}
.case-text{flex:1}
.case-text h3{font-size:19px;font-weight:700}
.case-text p{font-size:13px;color:var(--muted);margin-top:8px}
.case-more{align-self:flex-end;font-size:13px;border:1px solid var(--line);padding:5px 16px;white-space:nowrap}
.search{background:var(--pale);margin-top:40px;padding:0 0 30px}
.search-head{background:var(--ink);color:var(--white);padding:14px 20px;display:flex;align-items:center;gap:10px}
.search-head b{font-family:"Roboto",sans-serif;font-size:22px}
.search-head span{font-size:13px}
.search-form{padding:22px 60px 0}
.search-lead{font-size:13px;color:var(--muted);margin-bottom:12px}
.field{display:flex;align-items:center;height:50px;border-bottom:1px solid var(--line)}
.field label{width:150px;font-size:14px;font-weight:700}
.field .box{flex:1;height:32px;background:var(--white);border:1px solid var(--line);font-size:13px;color:var(--muted);padding:5px 10px;display:flex;justify-content:space-between}
.search-submit{display:block;width:300px;margin:24px auto 0;background:var(--red);color:var(--white);text-align:center;font-weight:700;padding:12px}
.points{display:grid;grid-template-columns:repeat(4,1fr);gap:14px;margin-top:18px}
.point-card{border:1px solid var(--line)}
.point-card .tag{background:var(--red);color:var(--white);font-family:"Roboto",sans-serif;font-size:13px;font-weight:700;padding:4px 10px}
.point-card .pic{height:120px;background:linear-gradient(135deg,#e2d7cb,#b8c4cf)}
.point-card h4{font-size:14px;padding:10px 10px 4px;line-height:1.45}
.point-card p{font-size:12px;color:var(--muted);padding:0 10px 12px}
.sns-row{display:grid;grid-template-columns:repeat(4,1fr);gap:12px;margin-top:36px}
.sns-row .sns-btn{height:62px;font-size:13px;line-height:1.3}
.news li{display:flex;gap:30px;border-bottom:1px dotted var(--line);padding:12px 4px;font-size:13px}
.news time{font-family:"Roboto",sans-serif;color:var(--muted)}
.group-grid{display:grid;grid-template-columns:repeat(4,1fr);gap:12px;margin-top:18px}
.group-grid div{height:52px;border:1px solid var(--line);display:flex;align-items:center;justify-content:center;gap:8px;font-weight:700;font-size:15px;color:var(--red)}
.group-grid div i{width:12px;height:12px;background:var(--red);display:block}

/* footer */
.site-map{background:var(--pale);margin-top:40px;height:560px;padding:44px 40px;display:flex;gap:30px}
.site-map .col{width:150px}
.site-map h5{font-size:13px;font-weight:700;border-bottom:1px solid var(--line);padding-bottom:5px;margin-bottom:8px}
.site-map li{font-size:12px;line-height:2.1;color:var(--ink)}
.site-map li::before{content:"・";color:var(--red)}
.footer-brand{margin-left:auto;align-self:flex-end;text-align:right}
.footer-brand .brand-name{font-size:36px}
.footer-brand .tel{font-family:"Roboto",sans-serif;font-size:26px;font-weight:700;color:var(--red)}
.footer-brand small{display:block;font-size:11px;color:var(--muted)}
.goods-visual{margin-top:40px;height:640px;background:linear-gradient(160deg,#f4f0ea 0%,#e6d2c0 35%,#c8d6e0 70%,#f1ece4 100%)}
.copyright{height:72px;display:flex;align-items:center;justify-content:center;font-size:12px;color:var(--muted);border-top:1px solid var(--line)}
</style>
</head>
<body>

<header class="site-header">
  <div class="brand">
    <span class="brand-mark"></span>
    <span class="brand-name">集客商会</span>
    <span class="brand-tag">ノベルティ・オリジナルグッズ制作・印刷・企画のお役立ち本舗</span>
  </div>
  <div class="contact">
    <small>運営:株式会社くみほ企画</small>
    <div class="tel">
      <svg width="28" height="28" viewBox="0 0 24 24" aria-hidden="true"><path fill="#d7000f" d="M6.6 10.8a15 15 0 0 0 6.6 6.6l2.2-2.2c.3-.3.7-.4 1-.2 1.1.4 2.3.6 3.6.6.6 0 1 .4 1 1V20c0 .6-.4 1-1 1A17 17 0 0 1 3 4c0-.6.4-1 1-1h3.5c.6 0 1 .4 1 1 0 1.3.2 2.5.6 3.6.1.3 0 .7-.2 1z"/></svg>
      0120-555-018
    </div>
    <div class="hours">TEL 078-000-0000 / FAX 078-000-0001 受付 平日9:00〜18:00</div>
  </div>
</header>

<nav class="global-nav">
  <a>名入れ・入稿データ</a><a>よくある質問</a><a>ご注文の流れ</a><a>ご入稿方法</a><a>送料・お支払い</a><a>スタッフ紹介</a><a>会社概要</a><a>お問い合わせ</a>
</nav>

<section class="hero">
  <div class="hero-goods" role="img" aria-label="タンブラー・ペン・エコバッグなどノベルティ商品の集合写真"></div>
  <div class="hero-person" role="img" aria-label="笑顔で案内する女性販促コンサルタントの写真"></div>
  <div class="hero-badge"><span>取引実績</span><strong>0000社</strong><span>突破!</span></div>
  <div class="hero-copy">
    <p>広告代理店様・イベント会社様のお助けサイト</p>
    <h1>販促×お悩み相談!=集客商会</h1>
  </div>
</section>

<section class="consult">
  <div class="consult-card">
    <div class="photo" role="img" aria-label="男性コンサルタントの写真"></div>
    <div><span class="label">担当者紹介</span><p>全国からの<br>お問い合わせは<br>私にお任せ下さい</p></div>
  </div>
  <div class="consult-card center">
    <p>販促品は<br>「販促品のプロ」に<br>ご相談ください</p>
  </div>
  <div class="consult-card">
    <div class="photo" role="img" aria-label="女性コンサルタントの写真"></div>
    <div><span class="label">担当者紹介</span><p>東京23区の<br>お問い合わせは<br>私にお任せ下さい</p></div>
  </div>
</section>

<div class="columns">
  <aside class="sidebar">
    <div class="side-head red">商品カテゴリー</div>
    <ul class="cat-list">
      <li><span class="thumb" role="img" aria-label="商品写真"></span>ウェットティッシュ</li>
      <li><span class="thumb" role="img" aria-label="商品写真"></span>付箋</li>
      <li><span class="thumb" role="img" aria-label="商品写真"></span>あぶらとり紙</li>
      <li><span class="thumb" role="img" aria-label="商品写真"></span>カレンダー</li>
      <li><span class="thumb" role="img" aria-label="商品写真"></span>クリアファイル</li>
      <li><span class="thumb" role="img" aria-label="商品写真"></span>ステーショナリー</li>
      <li><span class="thumb" role="img" aria-label="商品写真"></span>ボールペン</li>
      <li><span class="thumb" role="img" aria-label="商品写真"></span>スマホ・PC</li>
      <li><span class="thumb" role="img" aria-label="商品写真"></span>タオル</li>
      <li><span class="thumb" role="img" aria-label="商品写真"></span>トイレットペーパー</li>
      <li><span class="thumb" role="img" aria-label="商品写真"></span>エコバッグ</li>
      <li><span class="thumb" role="img" aria-label="商品写真"></span>マスク・衛生雑貨</li>
      <li><span class="thumb" role="img" aria-label="商品写真"></span>メモ</li>
      <li><span class="thumb" role="img" aria-label="商品写真"></span>入浴剤</li>
      <li><span class="thumb" role="img" aria-label="商品写真"></span>食品</li>
      <li><span class="thumb" role="img" aria-label="商品写真"></span>生活雑貨</li>
      <li><span class="thumb" role="img" aria-label="商品写真"></span>キッチン用品</li>
      <li><span class="thumb" role="img" aria-label="商品写真"></span>家庭用品・ギフト</li>
      <li><span class="thumb" role="img" aria-label="商品写真"></span>Tシャツ</li>
      <li><span class="thumb" role="img" aria-label="商品写真"></span>うちわ</li>
      <li><span class="thumb" role="img" aria-label="商品写真"></span>お菓子食品</li>
      <li><span class="thumb" role="img" aria-label="商品写真"></span>その他</li>
    </ul>

    <div class="side-block">
      <div class="side-head">集客商会<br>グループ専門店</div>
      <ul class="plain-list">
        <li>ポケットティッシュ工房</li><li>うちわ工房</li><li>カレンダー工房</li><li>メモ帳工房</li>
        <li>オリジナルのぼり工房</li><li>ウェットティッシュ工房</li><li>のぼり工房</li><li>扇子工房</li><li>紙袋工房</li>
      </ul>
    </div>

    <div class="side-block">
      <div class="side-head">価格帯で探す</div>
      <ul class="plain-list">
        <li>〜99円</li><li>100円〜199円</li><li>200円〜299円</li><li>300円〜499円</li><li>500円〜999円</li>
        <li>1,000円〜1,999円</li><li>2,000円〜4,999円</li><li>5,000円〜</li>
      </ul>
    </div>

    <div class="side-toggle"><span>行事・イベントで探す</span><span>+</span></div>
    <div class="side-toggle"><span>ターゲットで探す</span><span>+</span></div>
    <div class="side-toggle"><span>特集で探す</span><span>+</span></div>

    <div class="sns-stack">
      <div class="sns-btn" style="background:var(--sns-1)"><i></i>Photogram</div>
      <div class="sns-btn" style="background:var(--sns-2)"><i></i>Facenote</div>
      <div class="sns-btn" style="background:var(--sns-3)"><i></i>Chirper</div>
      <div class="sns-btn" style="background:var(--sns-4)"><i></i>Viewtube</div>
    </div>
  </aside>

  <main class="main">
    <div class="banners">
      <div style="background:linear-gradient(135deg,#e9c9a8,#c99575)" role="img" aria-label="あったかノベルティ特集のバナー写真">あったかノベルティ</div>
      <div style="background:linear-gradient(135deg,#8fb0c9,#c7d6e2)" role="img" aria-label="2018年カレンダー特集のバナー写真">Calendar 2018</div>
      <div style="background:linear-gradient(135deg,#b32a2a,#e07b6e)" role="img" aria-label="クリスマス特集のバナー写真">Christmas</div>
    </div>

    <div class="section-head"><h2>Achievement</h2><span>実績 — お客様のご要望と解決策をご紹介</span></div>
    <div class="achievement">
      <div class="case-label">case1</div>
      <div class="case-photo" role="img" aria-label="制作事例のノベルティ写真"></div>
      <div class="case-text">
        <h3>イベント用にオリジナルノベルティグッズを作りたい</h3>
        <p>株式会社○○様</p>
        <p>ここに実績の概要が入ります。ご相談内容とご提案の流れを簡潔にまとめて掲載します。ここに実績の概要が入ります。</p>
      </div>
      <div class="case-more">もっと見る</div>
    </div>

    <section class="search">
      <div class="search-head">
        <svg width="20" height="20" viewBox="0 0 24 24" aria-hidden="true"><circle cx="10" cy="10" r="7" fill="none" stroke="#fff" stroke-width="2.5"/><path d="M15 15l6 6" stroke="#fff" stroke-width="2.5"/></svg>
        <b>Search</b><span>目的で商品を探す</span>
      </div>
      <div class="search-form">
        <p class="search-lead">複数の条件から商品を探せます。キーワードでの絞り込みも可能です。</p>
        <div class="field"><label>商品カテゴリー</label><div class="box"><span>選択してください</span><span>▼</span></div></div>
        <div class="field"><label>行事・イベント</label><div class="box"><span>選択してください</span><span>▼</span></div></div>
        <div class="field"><label>ターゲット</label><div class="box"><span>選択してください</span><span>▼</span></div></div>
        <div class="field"><label>価格帯</label><div class="box"><span>選択してください</span><span>▼</span></div></div>
        <div class="field"><label>キーワード</label><div class="box"><span>キーワードを入力してください</span><span></span></div></div>
        <span class="search-submit">上記の内容で検索する</span>
      </div>
    </section>

    <div class="section-head"><h2>Point</h2><span>はじめての方でも安心!集客商会のおすすめポイント</span></div>
    <div class="points">
      <div class="point-card"><div class="tag">Point1</div><div class="pic" role="img" aria-label="スタッフ打ち合わせの写真"></div><h4>地域密着型スタッフがノベルティ販売に無料相談</h4><p>テキストが入ります。テキストが入ります。</p></div>
      <div class="point-card"><div class="tag">Point2</div><div class="pic" role="img" aria-label="配送作業の写真"></div><h4>緊急案件・お急ぎ案件にも迅速対応</h4><p>テキストが入ります。テキストが入ります。</p></div>
      <div class="point-card"><div class="tag">Point3</div><div class="pic" role="img" aria-label="商品サンプルの写真"></div><h4>低価格で豊富な商品ラインナップ</h4><p>テキストが入ります。テキストが入ります。</p></div>
      <div class="point-card"><div class="tag">Point4</div><div class="pic" role="img" aria-label="制作現場の写真"></div><h4>WEB販促担当者様の強い味方</h4><p>テキストが入ります。テキストが入ります。</p></div>
    </div>

    <div class="sns-row">
      <div class="sns-btn" style="background:var(--sns-1)"><i></i>Photogramで<br>実績公開中</div>
      <div class="sns-btn" style="background:var(--sns-2)"><i></i>Facenoteで<br>情報発信中</div>
      <div class="sns-btn" style="background:var(--sns-3)"><i></i>Chirperで<br>新着情報</div>
      <div class="sns-btn" style="background:var(--sns-4)"><i></i>Viewtubeで<br>商品紹介</div>
    </div>

    <div class="section-head"><h2>News</h2><span>お知らせ・新着情報</span></div>
    <ul class="news">
      <li><time>2017/11/00</time>ここにお知らせが入ります。ここにお知らせが入ります。</li>
      <li><time>2017/11/00</time>ここにお知らせが入ります。ここにお知らせが入ります。</li>
      <li><time>2017/11/00</time>ここにお知らせが入ります。ここにお知らせが入ります。</li>
      <li><time>2017/11/00</time>ここにお知らせが入ります。ここにお知らせが入ります。</li>
    </ul>

    <div class="section-head"><h2>Group</h2><span>集客商会グループ 運営専門サイト</span></div>
    <div class="group-grid">
      <div><i></i>ティッシュ工房</div><div><i></i>うちわ工房</div><div><i></i>ウェット工房</div><div><i></i>扇子工房</div>
      <div><i></i>ネットうちわ工房</div><div><i></i>メモ帳工房</div><div><i></i>カレンダー工房</div><div><i></i>カイロ工房</div>
      <div><i></i>クリアファイル工房</div><div><i></i>のぼり工房</div><div><i></i>オリジナル工房</div><div><i></i>紙袋工房</div>
    </div>
  </main>
</div>

<footer>
  <div class="site-map">
    <div class="col"><h5>商品カテゴリー</h5><ul><li>ウェットティッシュ</li><li>付箋</li><li>あぶらとり紙</li><li>カレンダー</li><li>クリアファイル</li><li>ボールペン</li><li>タオル</li><li>エコバッグ</li><li>マスク</li><li>メモ</li><li>食品</li><li>生活雑貨</li></ul></div>
    <div class="col"><h5>価格帯で探す</h5><ul><li>〜99円</li><li>100円〜199円</li><li>200円〜299円</li><li>300円〜499円</li><li>500円〜999円</li><li>1,000円〜</li></ul><h5 style="margin-top:14px">ターゲットで探す</h5><ul><li>男性向け</li><li>女性向け</li><li>ファミリー向け</li></ul></div>
    <div class="col"><h5>行事・イベントで探す</h5><ul><li>展示会</li><li>新年</li><li>決算</li><li>夏祭り</li><li>ハロウィン</li><li>クリスマス</li><li>セミナー</li></ul></div>
    <div class="col"><h5>集客商会グループ専門店</h5><ul><li>ティッシュ工房</li><li>うちわ工房</li><li>カレンダー工房</li><li>メモ帳工房</li><li>のぼり工房</li><li>扇子工房</li><li>紙袋工房</li></ul></div>
    <div class="col"><h5>ご利用ガイド</h5><ul><li>名入れ・入稿データ</li><li>よくある質問</li><li>ご注文の流れ</li><li>ご入稿方法</li><li>送料・お支払い</li><li>スタッフ紹介</li><li>会社概要</li><li>お問い合わせ</li></ul></div>
    <div class="footer-brand">
      <div class="brand"><span class="brand-mark" style="width:50px;height:50px"></span><span class="brand-name">集客商会</span></div>
      <div class="tel">0120-555-018</div>
      <small>TEL 078-000-0000 / FAX 078-000-0001</small>
    </div>
  </div>
  <div class="goods-visual" role="img" aria-label="エコバッグ・タンブラー・文具などオリジナルグッズを並べた商品写真"></div>
  <div class="copyright en">Copyright © 2000-2018 Kumiho Planning Co., Ltd. All rights Reserved.</div>
</footer>

</body>
</html>
```